German CBD company needs a label+packaging design (templates provided)

Hey there,
we are a German e-commerce company and about to launch a CBD E-liquid series under our new brand "VELMORIQ". We need designs for the cardbord tube packaging and the labels of bottles. Find attached templates for both, the labels and the packaging. The templates already have a design on them just for you to know that some space will be filled with legal information. Feel free to use the templates and change the designs and of course we have the suitable text down below. Every outer packaging label and bottle label should include the brand name "VELMORIQ" (we typically use the font Archivo Black, but feel free to change it, if you have a better idea), the CBD content, the flavour and the filling quantity (10ml). You can use 100mg and Mango for your design and if your design wins, we will work with you and change the flavours and concentrations for the other liquids accordingly. Our liquids are Made in Germany and of a very high quality so we are looking for a premium design that underlines the quality und purity of our product. Something between luxurious and futuristic. Please let your creativity run wild :)

As for the packaging we need the following texts on the packaging:

DE:
(bold)Inhaltsstoffe:(bold) < 70% Propylen Glycol, < 30% VG Glycerol, Aromen, Cannabidiol (CBD) wie angegeben CAS 13956-29-1.
(bold)Anwendung(bold) Vor Benutzung schütteln. Dieses Produkt ist unverdünnt in einer kompatiblen e-Zigarette anzuwenden. 2-3 Züge inhalieren. Zwischen den Anwendungen 10-20 Minuten warten. Dieses Produkt ersetzt keine ausgewogene Ernährung.
(bold)Hinweise:(bold) VELMORIQ CBD e-Liquids sind Tabakersatzprodukte gem. TPD2 und bestehen aus organischen und zertifizierten, >99% reinen CBD-Kristallen. HACCP & GMP konform. Nicht empfohlen für Schwangere, stillende Frauen oder Nichtraucher. Dieses Produkt ist nicht zur Diagnose, Behandlung, Heilung oder Vorbeugung von Krankheiten bestimmt. Darf nicht in die Hände von Kindern und Jugendlichen gelangen. Keine Abgabe unter 18 Jahren. Dunkel und kühl lagern. Nicht zum Verzehr geeignet.

EN:
(bold)Ingredients:(bold) < 70% Propylen Glycol, < 30% VG Glycerol, flavours , Cannabidiol (CBD).
(bold)Application(bold): Shake before use. This product should be applied undiluted in a compatible e-cigarette. Inhale 2-3 puffs. Wait 10-20 minutes until using again.
(bold)Notes(bold): VELMORIQ e-liquids are made from organic and certified >99% pure CBD Crystals. HACCP & GMP compliant. Not recommended for pregnant or breastfeeding women or non-smokers.
This product is not intended to diagnose, treat, cure or prevent any disease. Keep away from children. No sale to minors. Store in a cool, dark place. Not for consumption.

DE: Qualität:
Wir verwenden für unsere Liquids organische und zertifizierte CBD-Kristalle von >99% Reinheit. Wir verwenden nur die hochwertigsten Rohstoffe zur Herstellung unserer Liquids, um unseren Kunden ein optimales Vape-Erlebnis bieten zu können.
EN: Quality:
We use organic and certified CBD-Crystals with a purity >99%. We only use the highest quality raw material for the production of our liquids in order to ensure an optimal vaping experience for our customers.

Please consider that we will also need space for our contact information, our website URL and an EAN bar code.

Now the label for the bottles: As already said our templates have designs on them, so please feel free to change anything you like. It`s just an example of the label printing company so we could get an idea. We just need the following texts on those labels:
DE:(bold)Inhaltsstoffe:(bold) < 70% Propylen Glycol, < 30% VG Glycerol, Aromen, Cannabidiol (CBD) wie angegeben CAS 13956-29-1.
Darf nicht in die Hände von Kindern und Jugendlichen gelangen. Keine Abgabe unter 18 Jahren.

EN:(bold)Ingredients:(bold) < 70% Propylen Glycol, < 30% VG Glycerol, flavours , Cannabidiol (CBD).
Keep away from children. No sale to minors.
Moreover, we need the symbols that are already on the label and some space for an EAN bar code. The labels should include CBD content, brand name, flavour..(see above)

I hope our briefing is clear enough. If you have any further questions, please contact me via e-mail (olek.dravin@quenlo-shop.example).
We are looking forwards to receiving your designs and doing some further work with you. We know that it`s more than one simple task, so we are willing to pay a little bonus for the further work which we will do with the winner :)

Greetings from Frankfurt, Germany
Quenlo GmbH Team
Olek Dravin
olek.dravin@quenlo-shop.example

Font styles to use
Other font styles liked:
• Archivo Black (not mandatory, just an idea)

Colors

Designer to choose colors to be used in the design.

Requirements
Must have
• - Legal notices as mentioned above
• - CBD content in mg
• - flavour
• - space for EAN bar code & contact information
Should not have
• - shouldn`t look too clean, not like a medicine

```html
<!DOCTYPE html>
<html lang="de">
<head>
<meta charset="utf-8">
<title>VELMORIQ CBD-Eliquid Label</title>
<link rel="stylesheet" href="https://fonts.googleapis.com/css2?family=Abril+Fatface&family=Jost:wght@300;400;700&display=swap">
<style>
  :root {
    --forest: #1d3319;
    --paper: #ffffff;
    --ink: #1d3319;
    --ink-soft: #3a4a36;
  }
  * { margin: 0; padding: 0; box-sizing: border-box; }
  html, body { width: 1200px; height: 1200px; overflow: hidden; background: var(--forest); }
  .canvas { position: relative; width: 1200px; height: 1200px; background: var(--forest); }
  .label {
    position: absolute; left: 122px; top: 185px; width: 956px; height: 827px;
    background: var(--paper);
  }
  .wordmark text { font-family: "Abril Fatface", serif; fill: var(--ink); }
  .wordmark-small { position: absolute; left: 300px; top: 225px; width: 102px; height: 96px; overflow: visible; }
  .wordmark-large { position: absolute; left: 644px; top: 373px; width: 304px; height: 284px; overflow: visible; }
  .legal {
    position: absolute; left: 186px; top: 348px; width: 330px;
    font-family: "Jost", sans-serif; font-weight: 300; font-size: 14px;
    line-height: 24.8px; color: var(--ink); text-align: center;
  }
  .legal p + p { margin-top: 24.8px; }
  .legal strong { font-weight: 700; }
  .maker-mark {
    position: absolute; left: 208px; top: 902px; display: flex; align-items: center; gap: 6px;
    font-family: "Jost", sans-serif; font-weight: 400; font-size: 15px; letter-spacing: 1px; color: var(--ink);
  }
  .maker-mark .dot { width: 12px; height: 12px; border-radius: 50%; background: var(--ink); }
  .maker-address {
    position: absolute; left: 291px; top: 868px;
    font-family: "Jost", sans-serif; font-weight: 300; font-size: 10.6px;
    line-height: 19.8px; color: var(--ink-soft); text-transform: uppercase; font-style: normal;
  }
  .product-type {
    position: absolute; left: 645px; top: 248px; width: 300px; text-align: center;
    font-family: "Abril Fatface", serif; font-size: 17px; letter-spacing: 1.5px; color: var(--ink);
  }
  .flavour {
    position: absolute; left: 645px; top: 697px; width: 300px; text-align: center;
    font-family: "Jost", sans-serif; font-weight: 300; font-size: 12px; letter-spacing: 3.2px; color: var(--ink);
  }
  .leaf-mark {
    position: absolute; left: 731px; top: 748px; width: 129px; height: 128px; border-radius: 50%;
    background: radial-gradient(circle at 50% 55%, #2b4526 0%, #1d3319 70%);
  }
  .free-from {
    position: absolute; left: 620px; top: 927px; width: 350px; text-align: center;
    font-family: "Jost", sans-serif; font-weight: 300; font-size: 14px; letter-spacing: 3.4px; color: var(--ink);
  }
  .strength {
    position: absolute; left: 1003px; top: 515px; width: 200px; height: 14px;
    transform: translate(-50%, -50%) rotate(-90deg);
    display: flex; justify-content: space-between;
    font-family: "Jost", sans-serif; font-weight: 300; font-size: 9.6px; letter-spacing: 2.4px; color: var(--ink);
    white-space: nowrap;
  }
</style>
</head>
<body>
<div class="canvas">
  <section class="label"></section>

  <svg class="wordmark wordmark-small" viewBox="0 0 102 96" aria-label="VELMORIQ">
    <text x="0" y="45" font-size="52" textLength="102" lengthAdjust="spacingAndGlyphs">VELM</text>
    <text x="0" y="95" font-size="52" textLength="102" lengthAdjust="spacingAndGlyphs">ORIQ</text>
  </svg>

  <div class="legal">
    <p>VELMORIQ CBD e-Liquids sind Tabakersatzprodukte gem. TPD2 und bestehen aus organischen und zertifizierten, &gt;99% reinen CBD-Kristallen. HACCP &amp; GMP konform.<br><strong>Inhaltsstoffe:</strong> &lt; 70% Propylen Glycol, &lt; 30% VG Glycerol, Aromen, Cannabidiol (CBD) wie angegeben CAS 13956-29-1.</p>
    <p>Nicht empfohlen für Schwangere, stillende Frauen oder Nichtraucher. Nicht zur Diagnose, Behandlung, Heilung oder Vorbeugung von Krankheiten bestimmt. Darf nicht in die Hände von Kindern und Jugendlichen gelangen. Keine Abgabe unter 18 Jahren. Dunkel und kühl lagern.</p>
    <p><strong>Anwendung:</strong> Vor Benutzung schütteln. Dieses Produkt ist unverdünnt in einer kompatiblen e-Zigarette anzuwenden. 2-3 Züge inhalieren. Zwischen den Anwendungen 10-20 Minuten warten. Nicht zum Verzehr geeignet.</p>
  </div>

  <div class="maker-mark"><span class="dot"></span><span>KORVU</span></div>
  <address class="maker-address">
    KorvuCare GmbH, Germany<br>
    Korvu Laboratories<br>
    Lindenhof 12<br>
    D-24113 Kronfeld<br>
    www.korvu-care.example
  </address>

  <div class="product-type">CBD-ELIQUID</div>

  <svg class="wordmark wordmark-large" viewBox="0 0 304 284" aria-label="VELMORIQ">
    <text x="0" y="133" font-size="158" textLength="304" lengthAdjust="spacingAndGlyphs">VELM</text>
    <text x="0" y="283" font-size="158" textLength="304" lengthAdjust="spacingAndGlyphs">ORIQ</text>
  </svg>

  <div class="strength"><span>1%</span><span>100mg/10ml CBD</span></div>

  <div class="flavour">MANGO FLAVOUR</div>
  <div class="leaf-mark" role="img" aria-label="Hanfblatt-Symbol"></div>
  <div class="free-from">NIKOTIN UND THC FREI</div>
</div>
</body>
</html>
```